BrambleWorks business card

Looking for business card design that supports our company/software values. We have 2 logo designs at the moment but open to change if you think you can enhance the brand. Check out website www.brambleworks.com.au.

Target Market(s)

Education

Contact Information for Business Card

Name, title, mobile, email and website

Font styles to use
Sans Serif

Colors

Designer to choose colors to be used in the design.

Requirements
Must have
• BrambleWorks logo with tree and tagline on rear side with dark grey background colour

```html
<!DOCTYPE html>
<html lang="en">
<head>
<meta charset="utf-8">
<title>BrambleWorks Business Card</title>
<link href="https://fonts.googleapis.com/css2?family=Lato:wght@400;700&display=swap" rel="stylesheet">
<style>
  :root {
    --stage: #2b2e31;
    --card-light: #ffffff;
    --card-dark: #4a4b49;
    --ink: #2f3030;
    --ink-soft: #555656;
    --brand-green: #2e6b1f;
    --leaf-green: #5f9a45;
    --rule-green: #8fb27f;
    --white: #ffffff;
  }
  * { box-sizing: border-box; margin: 0; padding: 0; }
  html, body { width: 1200px; height: 900px; overflow: hidden; }
  body {
    background: var(--stage);
    font-family: "Lato", sans-serif;
    display: flex;
    align-items: center;
    justify-content: center;
    gap: 40px;
  }
  .card {
    width: 540px;
    height: 310px;
    border-radius: 4px;
    position: relative;
    overflow: hidden;
    box-shadow: 0 14px 30px rgba(0,0,0,0.35);
  }

  /* Front */
  .card--front { background: var(--card-light); display: flex; align-items: center; }
  .front__brand {
    width: 48%;
    display: flex;
    align-items: center;
    justify-content: center;
    gap: 10px;
  }
  .brand-dot {
    width: 18px; height: 18px; border-radius: 50%;
    background: var(--leaf-green);
    flex: none;
  }
  .front__brand .brand-name {
    font-size: 24px; font-weight: 400; color: var(--ink);
  }
  .front__divider {
    width: 1px; height: 130px; background: var(--rule-green);
  }
  .front__contact { padding-left: 30px; }
  .contact__name {
    font-size: 22px; font-weight: 700; color: var(--brand-green);
    letter-spacing: 0.5px; text-transform: uppercase;
  }
  .contact__title { font-size: 13px; color: var(--ink-soft); margin: 2px 0 14px; }
  .contact__list { list-style: none; }
  .contact__item {
    display: flex; align-items: center; gap: 10px;
    font-size: 15px; color: var(--ink); margin-bottom: 7px;
  }
  .contact__item svg { width: 14px; height: 14px; flex: none; }

  /* Back */
  .card--back { background: var(--card-dark); }
  .back__leaves {
    position: absolute; right: -40px; bottom: -60px;
    width: 380px; height: 300px;
    background: radial-gradient(ellipse at center, rgba(95,154,69,0.35), rgba(95,154,69,0) 70%);
  }
  .back__brand {
    position: absolute; left: 90px; top: 100px;
    display: flex; align-items: center; gap: 14px;
  }
  .back__brand .brand-dot { width: 26px; height: 26px; background: var(--leaf-green); }
  .back__wordmark { display: flex; flex-direction: column; }
  .back__brand .brand-name {
    font-size: 40px; font-weight: 400; color: var(--white);
    padding-bottom: 6px; border-bottom: 1px solid var(--white);
  }
  .brand-tagline { font-size: 15px; color: var(--white); margin-top: 5px; letter-spacing: 0.3px; }
</style>
</head>
<body>

  <section class="card card--front">
    <div class="front__brand">
      <span class="brand-dot"></span>
      <span class="brand-name">BrambleWorks</span>
    </div>
    <div class="front__divider"></div>
    <div class="front__contact">
      <h1 class="contact__name">Nora Hale</h1>
      <p class="contact__title">Position</p>
      <ul class="contact__list">
        <li class="contact__item">
          <svg viewBox="0 0 16 16"><path d="M4 1.5 6.3 4 5 6c.9 2 2.5 3.6 4.5 4.5l2-1.3 2.5 2.3-1.5 2.5C7 13.5 2.5 9 1.5 3z" fill="var(--brand-green)"/></svg>
          <span>123 456 7890</span>
        </li>
        <li class="contact__item">
          <svg viewBox="0 0 16 16"><rect x="1" y="3" width="14" height="10" fill="var(--brand-green)"/><path d="M1.5 3.5 8 9l6.5-5.5" fill="none" stroke="#fff" stroke-width="1.2"/></svg>
          <span>lorem@yourwebsite.com</span>
        </li>
        <li class="contact__item">
          <svg viewBox="0 0 16 16"><circle cx="8" cy="8" r="6.5" fill="none" stroke="var(--brand-green)" stroke-width="1.5"/><path d="M1.5 8h13M8 1.5c-3 3.5-3 9.5 0 13M8 1.5c3 3.5 3 9.5 0 13" fill="none" stroke="var(--brand-green)" stroke-width="1.2"/></svg>
          <span>www.yourwebsite.com</span>
        </li>
      </ul>
    </div>
  </section>

  <section class="card card--back">
    <div class="back__leaves" role="img" aria-label="Scattered falling green leaves decoration"></div>
    <div class="back__brand">
      <span class="brand-dot"></span>
      <div class="back__wordmark">
        <span class="brand-name">BrambleWorks</span>
        <span class="brand-tagline">Student Success Platform</span>
      </div>
    </div>
  </section>

</body>
</html>
```